Stonebell Inc Ad Design, trying to attract new customers

Please see attached pictures and files for information
We are a Class A - Residential General Contractor in Lynchburg, VA with Master HVAC and Master PLUMBING Licenses. We focus on Water and Air Solutions for property owners.
We build, remodel, and repair homes
We do HVAC, including Humidity Control and Air Purification
We do Plumbing
We love to fix Water Leaks for Plumbing, Roof Leaks, Skylight Leaks, Basement Leaks, Foundation Leaks, Door and Window Leaks
We solve water and air issues on the outside of properties with custom structures, grading, and landscaping

Target Market(s)

Residential and Light Commercial property owners

Industry/Entity Type

Construction

Font styles to use
Other font styles liked:
• see cards

Colors
0054AA
0677BA
7BADD7
CADEEF
E8F1F8
00AB8E
00BBA5
67D7C9
C6EFE9
E9F9F6

Requirements
Must have
• See business cards
Nice to have
• see business cards
Should not have
• My name

```html
<!DOCTYPE html>
<html lang="en">
<head>
<meta charset="utf-8">
<title>Stonebell Inc – Billboard</title>
<link rel="stylesheet" href="https://fonts.googleapis.com/css2?family=Exo+2:wght@500;600;700;800&family=Michroma&display=swap">
<style>
  :root {
    --blue-deep: #0054AA;
    --blue: #0677BA;
    --blue-soft: #7BADD7;
    --blue-pale: #CADEEF;
    --blue-mist: #E8F1F8;
    --green: #6DBE2E;
    --white: #FFFFFF;
    --paper-edge: #E9ECEF;
    --stage: #F2F4F6;
  }
  * { box-sizing: border-box; margin: 0; padding: 0; }
  html, body { width: 1200px; height: 1200px; overflow: hidden; background: var(--stage); }
  .canvas { position: relative; width: 1200px; height: 1200px; }

  .billboard {
    position: absolute; left: 40px; top: 250px; width: 1120px; height: 700px;
    background: linear-gradient(135deg, var(--white) 35%, var(--paper-edge) 100%);
    overflow: hidden; font-family: "Exo 2", sans-serif;
    box-shadow: 0 6px 24px rgba(0,0,0,.12);
  }

  .header-band { position: absolute; left: 0; top: 0; width: 1120px; height: 151px; }
  .header-text {
    position: absolute; left: 330px; right: 20px; top: 0; height: 151px;
    display: flex; flex-direction: column; justify-content: center; align-items: center;
    color: var(--white); font-weight: 800; text-align: center; line-height: 1.2;
  }
  .tagline { font-size: 40px; }
  .license { font-size: 40px; }

  .brand {
    position: absolute; left: 30px; top: 52px; display: flex; align-items: center; gap: 10px;
  }
  .brand-dot { width: 34px; height: 34px; border-radius: 50%; background: var(--blue); }
  .brand-name { font-family: "Exo 2", sans-serif; font-weight: 800; font-size: 30px; color: var(--blue); letter-spacing: 1px; }

  .services {
    position: absolute; left: 0; right: 0; top: 180px;
    list-style: none; text-align: center;
    font-family: "Michroma", sans-serif; color: var(--blue-deep);
    font-size: 27px; line-height: 46px; white-space: nowrap;
    -webkit-text-stroke: 0.6px var(--blue-deep);
  }

  .footer-field {
    position: absolute; left: 365px; right: 0; top: 470px; bottom: 0;
    background: linear-gradient(180deg, var(--white) 0%, var(--blue-pale) 55%, var(--blue) 100%);
  }

  .scripture {
    position: absolute; left: 0; top: 478px; width: 365px; bottom: 0;
    background: linear-gradient(90deg, var(--blue-soft) 0, var(--blue-mist) 28px, var(--white) 30px);
    padding: 28px 14px 0 44px; text-align: center; color: var(--blue-deep);
    font-size: 11.5px; line-height: 17px;
  }
  .scripture-ref, .scripture-version { font-weight: 700; }
  .scripture-ref { margin-bottom: 6px; }
  .scripture-body { color: var(--blue); }
  .scripture-version { margin-top: 4px; }

  .contact-card {
    position: absolute; left: 394px; top: 482px; width: 703px; height: 191px;
    border: 4px solid var(--green); border-radius: 20px; overflow: hidden;
    background: var(--white); display: flex; flex-direction: column;
  }
  .phone {
    flex: 1; display: flex; align-items: center; justify-content: center;
    font-size: 84px; font-weight: 800; color: var(--blue-deep); letter-spacing: 1px;
  }
  .contact-strip {
    height: 74px; background: var(--blue-deep); display: flex; align-items: center;
    color: var(--white); font-weight: 500;
  }
  .contact-links { flex: 1.35; text-align: center; font-size: 20px; line-height: 28px; }
  .contact-divider { width: 2px; height: 54px; background: var(--white); }
  .contact-status { flex: 1; text-align: center; font-size: 20px; }
</style>
</head>
<body>
<div class="canvas">
  <section class="billboard" aria-label="Stonebell Inc billboard">
    <svg class="header-band" viewBox="0 0 1120 151" aria-hidden="true">
      <defs>
        <linearGradient id="band-fill" x1="0" y1="0" x2="1" y2="0">
          <stop offset="0.3" stop-color="#0054AA"/>
          <stop offset="0.65" stop-color="#2E8C8E"/>
          <stop offset="1" stop-color="#6DBE2E"/>
        </linearGradient>
      </defs>
      <path d="M272 0 H1120 V151 H425 C335 151 282 90 272 0 Z" fill="url(#band-fill)"/>
    </svg>

    <div class="brand">
      <span class="brand-dot"></span>
      <span class="brand-name">STONEBELL</span>
    </div>

    <div class="header-text">
      <p class="tagline">“We put Water and Air in its Place”</p>
      <p class="license">Class A RBC PLUMBINGHVAC</p>
    </div>

    <ul class="services">
      <li>HUMIDITY CONTROL/AIR PURIFICATION</li>
      <li>ROOF/SKYLIGHT LEAKS</li>
      <li>BASEMENT/FOUNDATION LEAKS</li>
      <li>DRAINAGE/GRADING/LANDSCAPING</li>
      <li>CUSTOM OUTDOOR STRUCTURES - PORCHES</li>
      <li>DECKS • SUNROOMS • GAZEBOS</li>
    </ul>

    <div class="footer-field"></div>

    <aside class="scripture">
      <p class="scripture-ref">PSALM 1:1-3</p>
      <p class="scripture-body">Blessed is the man who walks not in the counsel of the ungodly, nor stands in the path of sinners, nor sits in the seat of the scornful; but his delight is in the law of the <b>LORD</b>, and in His law he meditates day and night. He shall be like a tree planted by the rivers of water, that brings forth fruit in its season, whose leaf shall not wither, and whatever he does shall prosper</p>
      <p class="scripture-version">NKJV</p>
    </aside>

    <div class="contact-card">
      <p class="phone">(434) 555-0187</p>
      <div class="contact-strip">
        <div class="contact-links">
          <p>Contact@StonebellVA.com</p>
          <p>www.ShadeCraftVA.com</p>
        </div>
        <span class="contact-divider"></span>
        <p class="contact-status">Licensed and Insured</p>
      </div>
    </div>
  </section>
</div>
</body>
</html>
```